Hello - we need a label design for our Quillon Health Hair Loss supplement. It is a natural hair loss supplement for black/african american women to regrow new hair and help restore hair loss & thinning hair due to vitamin deficiencies, traction alopecia, etc. It is a science based efficacious supplement with a centuries old medicinal herbal formula.
Attached is the logo & files of other generic competition and also Black hair products for your perusal. The label has to be a upscale and have an ethnic flair to it. The product is clinically effective, leveraged by Ancient Wisdom and Modern Science. The front of the label should include the following:
Quillon Health (logo)
Crown Revitalizer
Advanced Women’s Hair Loss Formula
TRACTION ALOPECIA THERAPY
- Prevents hair loss & restores thinning, fragile hair
- Promotes Natural Hair Growth
- Strengthens Hair for less breakage
- Visibly increases hair density & thickness
- Thicker, Stronger, Longer, Hydrated hair
- Promotes Follicle regeneration & Hair Growth
Site-Specific for hair loss & stunted growth
60 capsules 30-day supply
Target Market(s)
Black/African American Women
Look and feel

```html
<!DOCTYPE html>
<html lang="en">
<head>
<meta charset="utf-8">
<title>Quillon Health – Crown Revitalizer Label</title>
<link href="https://fonts.googleapis.com/css2?family=Montserrat:ital,wght@0,300;0,400;0,600;0,700;0,800;1,500&display=swap" rel="stylesheet">
<style>
  :root {
    --page: #ffffff;
    --label-light: #e4e4e4;
    --label-light-2: #d6d6d6;
    --label-red: #c95a60;
    --label-red-deep: #b9444c;
    --banner-red: #d9444d;
    --gold-light: #d7a440;
    --gold-dark: #8a5a12;
    --ink: #2a1a14;
    --blush: #f6dada;
    --white: #ffffff;
  }
  * { box-sizing: border-box; margin: 0; padding: 0; }
  html, body { width: 1200px; height: 1200px; overflow: hidden; background: var(--page); }
  body { position: relative; font-family: 'Montserrat', sans-serif; }

  .label {
    position: absolute; left: 160px; top: 50px; width: 880px; height: 1100px;
    background: linear-gradient(90deg, var(--label-light-2), var(--label-light) 30%, var(--label-light) 70%, var(--label-light-2));
    overflow: hidden;
  }
  .label__diagonal { position: absolute; inset: 0; width: 100%; height: 100%; }

  .brand {
    position: absolute; top: 120px; left: 0; width: 100%;
    display: flex; justify-content: center; align-items: center; gap: 14px;
  }
  .brand__dot { width: 22px; height: 22px; border-radius: 50%; background: var(--ink); }
  .brand__name { font-weight: 400; font-size: 36px; color: var(--ink); letter-spacing: 1px; }

  .title {
    position: absolute; left: 0; width: 100%; text-align: center;
    font-weight: 800; font-size: 96px; line-height: 1;
    background: linear-gradient(180deg, var(--gold-light), var(--gold-dark));
    -webkit-background-clip: text; background-clip: text; color: transparent;
    filter: drop-shadow(3px 3px 0 #3a2410);
  }
  .title--line1 { top: 262px; }
  .title--line2 { top: 378px; }

  .formula-banner {
    position: absolute; left: 106px; top: 494px; width: 620px; height: 112px;
    background: var(--banner-red); color: var(--white);
    display: flex; flex-direction: column; justify-content: center; align-items: center;
    font-weight: 400; font-size: 40px; line-height: 1.12; letter-spacing: 3px;
  }

  .hair-art {
    position: absolute; left: 6px; top: 580px; width: 320px; height: 340px;
    background: radial-gradient(ellipse at 50% 55%, rgba(30,20,20,0.55), rgba(30,20,20,0.08) 70%, transparent 75%);
  }

  .therapy {
    position: absolute; left: 305px; top: 664px; width: 560px; color: var(--ink);
  }
  .therapy__heading { font-weight: 700; font-size: 25px; letter-spacing: 0.2px; margin-bottom: 8px; }
  .therapy__list { list-style: none; font-style: italic; font-weight: 500; font-size: 19px; line-height: 24.5px; }
  .therapy__list li:nth-child(2) { padding-left: 10px; }
  .therapy__list li:nth-child(3) { padding-left: 20px; }
  .therapy__list li:nth-child(4) { padding-left: 32px; }
  .therapy__list li:nth-child(5) { padding-left: 42px; }
  .therapy__list li:nth-child(6) { padding-left: 52px; }

  .site-specific {
    position: absolute; left: 365px; top: 874px; color: var(--blush);
    font-weight: 700; font-size: 27px; line-height: 1.1; text-align: left;
  }
  .site-specific span { display: block; padding-left: 18px; }

  .supply-bar {
    position: absolute; left: 81px; top: 958px; width: 713px; height: 54px;
    background: linear-gradient(180deg, var(--gold-light), var(--gold-dark));
    display: flex; justify-content: space-between; align-items: center; padding: 0 22px 0 30px;
    color: var(--ink); font-weight: 600; font-size: 26px;
  }
  .supply-bar__count { font-weight: 400; font-size: 22px; }
  .supply-bar__count b { font-weight: 700; font-size: 28px; }
</style>
</head>
<body>
  <main class="label">
    <svg class="label__diagonal" viewBox="0 0 880 1100" preserveAspectRatio="none" aria-hidden="true">
      <defs>
        <linearGradient id="redField" x1="0" y1="0" x2="1" y2="0">
          <stop offset="0" stop-color="#d65c63"/>
          <stop offset="0.6" stop-color="#c95a60"/>
          <stop offset="1" stop-color="#b9444c"/>
        </linearGradient>
      </defs>
      <polygon points="845,0 880,0 880,1100 0,1100 0,1045" fill="url(#redField)"/>
    </svg>

    <div class="brand">
      <span class="brand__dot"></span>
      <span class="brand__name">Quillon Health</span>
    </div>

    <h1 class="title title--line1">CROWN</h1>
    <h1 class="title title--line2">REVITALIZER</h1>

    <div class="formula-banner">
      <span>ADVANCED WOMEN’S</span>
      <span>HAIR LOSS FORMULA</span>
    </div>

    <div class="hair-art" role="img" aria-label="Line illustration of a woman's flowing hair"></div>

    <section class="therapy">
      <h2 class="therapy__heading">TRACTION ALOPECIA THERAPY</h2>
      <ul class="therapy__list">
        <li>- Prevents Hair Loss &amp; Restores Thinning, Fragile Hair</li>
        <li>- Promotes Natural Hair Growth</li>
        <li>- Strengthens Hair For Less Breakage</li>
        <li>- Visibly Increases Hair Density &amp; Thickness</li>
        <li>- Thicker, Stronger, Longer, Hydrated Hair</li>
        <li>- Promotes Follicle Regeneration &amp; Hair Growth</li>
      </ul>
    </section>

    <p class="site-specific">SITE-SPECIFIC FOR HAIR LOSS<span>&amp; STUNTED GROWTH</span></p>

    <div class="supply-bar">
      <span class="supply-bar__type">DIETARY SUPPLEMENT</span>
      <span class="supply-bar__count"><b>60</b> capsules / <b>30</b>-day supply</span>
    </div>
  </main>
</body>
</html>
```